Up to the Challenge? Canadian based consulting company needs a two sided business card design

A Canadian based security risk management consulting company needs a two-sided business card design. What we do is provide advice and guidance related to emergency, security and business continuity management for small, medium and large companies to help ensure the protection of their people, assets, information, services, operations and reputation.

The final design should be simple, only one or two colours, eye catching, professional and one that makes people look at three or more times just because it looks so darn good.

I have include examples of business cards I like.

Target Market(s)

Small, medium and large companies.

Industry/Entity Type

Security

Contact Information for Business Card

Business Card Size: Standard size of 3.5" (89mm) x 2.0" (51mm) - (see full specifications and guides on PRINTA's website if required)
Card Stock: Looking to use PRINTA's Velda 32pt stock textured paper - seam colour either chili red or black
Business Name: The Harrowfield Group
Website: www.theharrowfieldgroup.example
Telephone: (555)214-0397
Name: Dana Forsythe
Position: Principle
e-mail: Dana.Forsythe@theharrowfieldgroup.example

Font styles to use
Serif

Colors
ec1f27
000000
9d9d9d
aaaaaa
606060

Requirements
Must have
• - "The Harrowfield Group" logo (see uploaded files). I have included grey scale and colour versions.
• - Business card details (as above)
Nice to have
• - One side black or grey scale.
• - Other side would likely be white.
• - Everyone likes the silver logo on the black background.
• - Small element of colour i.e. red but I'm leaning more to greyscale.
Should not have
• - A lot of colour. Keep it simple.

```html
<!DOCTYPE html>
<html lang="en">
<head>
<meta charset="utf-8">
<title>The Harrowfield Group — Business Card</title>
<link rel="stylesheet" href="https://fonts.googleapis.com/css2?family=Noto+Serif:wght@400&display=swap">
<style>
  :root {
    --page: #ffffff;
    --shadow: #404040;
    --card-front: #909d9c;
    --card-back: #ffffff;
    --ink: #333333;
    --ink-brand: #3b3b3b;
    --edge: #2e2e2e;
  }
  html, body {
    margin: 0;
    padding: 0;
    width: 1200px;
    height: 1200px;
    overflow: hidden;
    background: var(--page);
    font-family: "Noto Serif", Georgia, serif;
  }
  .canvas {
    position: relative;
    width: 1200px;
    height: 1200px;
  }
  .card-shadow {
    position: absolute;
    width: 480px;
    height: 840px;
    background: var(--shadow);
  }
  .card-shadow.front { left: 102px; top: 255px; }
  .card-shadow.back  { left: 665px; top: 152px; }

  .card {
    position: absolute;
    width: 480px;
    height: 840px;
    box-sizing: border-box;
  }
  .card.front {
    left: 78px;
    top: 231px;
    background: var(--card-front);
  }
  .card.back {
    left: 641px;
    top: 128px;
    background: var(--card-back);
    border: 1px solid var(--edge);
  }
  .centered {
    position: absolute;
    left: 0;
    width: 100%;
    text-align: center;
    white-space: nowrap;
    color: var(--ink);
  }

  .brand-mark {
    position: absolute;
    left: 200px;
    top: 578px;
    width: 80px;
    height: 80px;
    background: var(--ink-brand);
  }
  .brand-name {
    top: 686px;
    font-size: 27px;
    line-height: 1.25;
    letter-spacing: 1px;
    color: var(--ink-brand);
  }
  .brand-name .sub {
    display: block;
    font-size: 18px;
    letter-spacing: 5px;
  }
  .website {
    top: 801px;
    font-size: 18px;
  }

  .person-name {
    top: 600px;
    font-size: 38px;
    letter-spacing: 0.5px;
  }
  .person-title {
    top: 691px;
    font-size: 31px;
  }
  .person-phone {
    top: 731px;
    font-size: 31px;
  }
  .person-email {
    top: 780px;
    font-size: 17px;
  }
</style>
</head>
<body>
<main class="canvas">
  <div class="card-shadow front"></div>
  <section class="card front" aria-label="Card front">
    <div class="brand-mark"></div>
    <div class="centered brand-name">THE HARROWFIELD<span class="sub">GROUP</span></div>
    <div class="centered website">www.theharrowfieldgroup.example</div>
  </section>

  <div class="card-shadow back"></div>
  <section class="card back" aria-label="Card back">
    <div class="centered person-name">DANA FORSYTHE</div>
    <div class="centered person-title">PRINCIPLE</div>
    <div class="centered person-phone">(555)214-0397</div>
    <div class="centered person-email">Dana.Forsythe@theharrowfieldgroup.example</div>
  </section>
</main>
</body>
</html>
```